Prescription Savings Card

Looking to revamp our cards that are distributed to pharmacies. Processing information must stand out and be in black with lines through zeros for easy identification.
I have included some previous card designs for consideration. we are looking to go with something cleaner with mainly processing information on the back similar to all white version attached.
Target Market(s)
Pharmacists and Pharmacy Technicians
Industry/Entity Type
prescription medications
Contact Information for Business Card
processing information
Requirements
Must have
- easy to read processing information

```html
<!DOCTYPE html>
<html lang="en">
<head>
<meta charset="utf-8">
<title>MedSaver Prescription Savings Card</title>
<link rel="stylesheet" href="https://fonts.googleapis.com/css2?family=Montserrat:wght@500;600;700;800;900&display=swap">
<style>
  :root {
    --backdrop: #b8b4aa;
    --card: #f3f3f3;
    --brand-blue: #3b4c84;
    --brand-red: #c8373c;
    --ink: #1c1c1c;
    --white: #ffffff;
  }
  * { box-sizing: border-box; margin: 0; padding: 0; }
  html, body {
    width: 1200px; height: 2400px; overflow: hidden;
    background: var(--backdrop);
    font-family: "Montserrat", sans-serif;
  }
  .canvas { position: relative; width: 1200px; height: 2400px; }
  .card {
    position: absolute; left: 88px; width: 1025px; height: 639px;
    background: var(--card); border-radius: 18px; overflow: hidden;
  }
  .card-front { top: 112px; }
  .card-back { top: 872px; }

  .headline-box {
    position: absolute; left: 40px; top: 47px; width: 517px; height: 147px;
    background: var(--brand-blue); color: var(--white);
    display: flex; align-items: center; justify-content: center;
    font-weight: 900; font-size: 44px; line-height: 1.02; letter-spacing: 0.5px;
  }
  .brand-name {
    position: absolute; left: 40px; color: var(--brand-blue);
    font-weight: 800; letter-spacing: -2px; line-height: 1;
  }
  .card-front .brand-name { top: 320px; font-size: 78px; }
  .card-back .brand-name { top: 58px; font-size: 92px; }
  .pricing-band {
    position: absolute; left: 40px; top: 525px; width: 517px; height: 68px;
    background: var(--brand-red); color: var(--white);
    display: flex; flex-direction: column; align-items: center; justify-content: center;
    font-weight: 700; font-size: 21px; line-height: 1.35;
  }
  .pricing-band .site { font-weight: 800; font-size: 20px; }
  .swoosh { position: absolute; inset: 0; width: 100%; height: 100%; }

  .processing {
    position: absolute; left: 678px; top: 38px; width: 307px;
    color: var(--ink); font-weight: 600; font-size: 34px; line-height: 45.5px;
  }
  .processing-row { display: flex; justify-content: space-between; }
  .benefits {
    position: absolute; left: 0; right: 0; top: 288px;
    text-align: center; color: var(--ink);
    font-weight: 600; font-size: 30px; line-height: 42.5px;
  }
  .pharmacy-notice {
    position: absolute; left: 40px; top: 499px; width: 945px; height: 94px;
    background: var(--brand-red); color: var(--white);
    display: flex; flex-direction: column; align-items: center; justify-content: center;
    text-align: center; font-weight: 600; font-size: 19.5px; line-height: 1.3;
  }
  .pharmacy-notice .title { font-weight: 500; }
</style>
</head>
<body>
<main class="canvas">
  <section class="card card-front" aria-label="Card front">
    <svg class="swoosh" viewBox="0 0 1025 639" preserveAspectRatio="none" aria-hidden="true">
      <path d="M783 0 Q980 320 776 639 L1025 639 L1025 0 Z" fill="var(--brand-red)"/>
      <path d="M870 0 Q1070 320 862 639 L1025 639 L1025 0 Z" fill="var(--brand-blue)"/>
    </svg>
    <div class="headline-box"><span>PRESCRIPTIONS<br>AT A DISCOUNT</span></div>
    <div class="brand-name">MedSaver</div>
    <div class="pricing-band">
      <span>Check Current Pricing on our Website</span>
      <span class="site">MedSaverCard.com</span>
    </div>
  </section>

  <section class="card card-back" aria-label="Card back">
    <div class="brand-name">MedSaver</div>
    <dl class="processing">
      <div class="processing-row"><dt>BIN:</dt><dd>014720</dd></div>
      <div class="processing-row"><dt>ID:</dt><dd>RX0000</dd></div>
      <div class="processing-row"><dt>PCN:</dt><dd>MDSV2</dd></div>
      <div class="processing-row"><dt>Group:</dt><dd>MEDSAV</dd></div>
      <div class="processing-row"><dt>Condor:</dt><dd>36805</dd></div>
    </dl>
    <ul class="benefits" style="list-style:none">
      <li>Save up to 99%</li>
      <li>100% HIPAA Compliant</li>
      <li>Lower Price Guarantee</li>
      <li>Covers 90 Days Supply &amp; Pet Meds</li>
    </ul>
    <div class="pharmacy-notice">
      <span class="title">ATTENTION PHARMACY</span>
      <span>If you are unable to process a prescription through our program please call (800)-555-0142</span>
      <span>Administrated by Meridian Claims - This is NOT INSURANCE</span>
    </div>
  </section>
</main>
</body>
</html>
```